mobile app - telecom industry

We are a tech/service company. Our product is a mobile application for physical site inspection called “Veko”. Our target industry is telecommunica...

Target Market(s)

telecommunication

Industry/Entity Type

Industry

Requirements
Must have
• Screen size Nimbus 5 - Android
• Suggest 3 colors
• Design 9 pages

```html
<!DOCTYPE html>
<html lang="en">
<head>
<meta charset="utf-8">
<title>Veko – Site Inspection App Screens</title>
<link href="https://fonts.googleapis.com/css2?family=Roboto:wght@400;500&display=swap" rel="stylesheet">
<style>
:root{
  --page:#f7f7f7;
  --blue:#6688db;
  --blue-light:#86abee;
  --blue-pale:#a9c4f5;
  --blue-dark:#4e6fc2;
  --pink:#f4a4aa;
  --pink-dark:#d9686e;
  --green:#4cd964;
  --ink:#222;
  --muted:#555;
  --line:#d9d9d9;
  --white:#fff;
}
*{box-sizing:border-box;margin:0;padding:0}
html,body{width:1056px;height:1200px;overflow:hidden}
body{background:var(--page);font-family:'Roboto',sans-serif;position:relative;color:var(--ink)}
.screen{position:absolute;width:293px;height:520px;background:var(--white);overflow:hidden;box-shadow:0 12px 22px rgba(0,0,0,.12)}
.s-splash{left:46px;top:50px}
.s-menu{left:379px;top:50px;background:var(--blue-light)}
.s-open{left:712px;top:50px}
.s-closed{left:46px;top:618px}
.s-form{left:379px;top:618px}
.s-saving{left:712px;top:618px}
.abs{position:absolute}
.scene{position:absolute;left:0;top:0;width:100%}
.brand{position:absolute;font-weight:500;color:var(--white);font-size:19px;letter-spacing:1px}
.back{position:absolute;left:14px;width:18px;height:14px}
.header-title{position:absolute;left:16px;color:var(--white);font-size:16px}
/* splash */
.s-splash .scene{height:350px;background:linear-gradient(180deg,var(--blue-light) 0%,var(--blue-pale) 55%,#c6d6f3 80%,var(--white) 100%)}
.s-splash .brand{left:0;width:100%;text-align:center;top:385px;font-size:38px;color:var(--blue);letter-spacing:3px}
/* menu */
.s-menu .scene{height:308px;background:linear-gradient(180deg,var(--blue-light) 0%,var(--blue-pale) 60%,#8fb0ee 100%)}
.tile{position:absolute;background:var(--white);display:flex;flex-direction:column;align-items:center;justify-content:center;gap:8px;color:var(--blue);font-size:11.5px;border:1px solid #c9d8f5}
.tile svg{width:24px;height:24px}
.tile.wide{flex-direction:row;gap:10px}
/* lists */
.head-blue{height:120px;background:linear-gradient(180deg,var(--blue-pale),var(--blue-light))}
.head-pink{height:120px;background:linear-gradient(180deg,#f8c2c5,var(--pink) 70%,var(--pink-dark))}
.wo-code{position:absolute;left:26px;color:var(--blue);font-size:13.5px}
.wo-date{position:absolute;left:26px;color:var(--muted);font-size:13.5px}
.wo-type{position:absolute;left:158px;color:var(--ink);font-size:13.5px}
.wo-num{position:absolute;left:158px;color:var(--muted);font-size:13.5px}
.trash{position:absolute;left:248px;width:14px;height:17px}
.divider{position:absolute;left:9px;right:12px;height:1px;background:var(--line)}
/* form */
.head-form{height:64px;background:linear-gradient(180deg,var(--blue-pale),var(--blue-light))}
.q-title{position:absolute;left:24px;font-size:13.5px;color:var(--ink)}
.q-title span{color:var(--blue)}
.tools{position:absolute;left:32px;display:flex;gap:26px}
.tools svg{width:16px;height:16px}
.comment{position:absolute;left:22px;width:251px;height:29px;background:var(--blue);color:var(--white);font-size:11.5px;display:flex;align-items:center;justify-content:center}
.btn{position:absolute;top:475px;height:39px;color:var(--white);font-size:12px;display:flex;align-items:center;justify-content:center}
.btn-save{left:5px;width:137px;background:var(--blue)}
.btn-close{left:150px;width:138px;background:var(--green)}
.overlay{position:absolute;inset:0;background:rgba(20,20,20,.68)}
.dialog{position:absolute;left:22px;top:171px;width:248px;height:147px;background:var(--white);border-radius:3px;display:flex;flex-direction:column;align-items:center;justify-content:center;gap:18px;font-size:13.5px}
.dialog svg{width:54px;height:54px}
</style>
</head>
<body>

<!-- Splash -->
<section class="screen s-splash">
  <div class="scene" role="img" aria-label="Illustration of a telecom tower among clouds and city buildings"></div>
  <div class="brand">Veko</div>
</section>

<!-- Main menu -->
<section class="screen s-menu">
  <div class="scene" role="img" aria-label="Illustration of a large telecom tower on a hill with clouds"></div>
  <svg class="back" style="top:37px" viewBox="0 0 18 14" fill="none" stroke="#fff" stroke-width="1.6"><path d="M17 7H2M7 1L1 7l6 6"/></svg>
  <div class="brand" style="left:44px;top:32px">Veko</div>
  <div class="tile" style="left:5px;top:310px;width:139px;height:73px">
    <svg viewBox="0 0 24 24"><rect x="2" y="3" width="5" height="18" fill="none" stroke="#6688db" stroke-width="1.5"/><rect x="8" y="3" width="14" height="18" fill="#6688db"/></svg>Open WO</div>
  <div class="tile" style="left:149px;top:310px;width:139px;height:73px">
    <svg viewBox="0 0 24 24"><rect x="3" y="3" width="18" height="18" fill="#6688db"/><path d="M8 8l8 8M16 8l-8 8" stroke="#fff" stroke-width="2"/></svg>Close WO</div>
  <div class="tile" style="left:5px;top:388px;width:139px;height:74px">
    <svg viewBox="0 0 24 24" fill="none" stroke="#6688db" stroke-width="2.2"><path d="M4 11a8 8 0 0 1 14-4l2 2M20 13a8 8 0 0 1-14 4l-2-2"/><path d="M20 4v5h-5M4 20v-5h5"/></svg>Syncronize</div>
  <div class="tile" style="left:149px;top:388px;width:139px;height:74px">
    <svg viewBox="0 0 24 24"><circle cx="12" cy="12" r="10" fill="#6688db"/><path d="M12 7v10M7 12h10" stroke="#fff" stroke-width="2.4"/></svg>Create WO</div>
  <div class="tile wide" style="left:5px;top:466px;width:283px;height:50px">
    <svg viewBox="0 0 24 24"><circle cx="12" cy="12" r="8" fill="none" stroke="#6688db" stroke-width="5" stroke-dasharray="3 2.3"/><circle cx="12" cy="12" r="6" fill="#6688db"/><circle cx="12" cy="12" r="2.5" fill="#fff"/></svg>Settings</div>
</section>

<!-- Open work orders -->
<section class="screen s-open">
  <div class="scene head-blue" role="img" aria-label="Header illustration of a telecom tower and city skyline"></div>
  <svg class="back" style="top:38px" viewBox="0 0 18 14" fill="none" stroke="#fff" stroke-width="1.6"><path d="M17 7H2M7 1L1 7l6 6"/></svg>
  <div class="brand" style="left:44px;top:33px">Veko</div>
  <div class="header-title" style="top:78px">Open Work Orders</div>
  <div class="wo-code" style="top:141px">TH1157-A</div><div class="wo-type" style="top:141px">TSSR</div>
  <div class="wo-date" style="top:163px">2017-10-25</div><div class="wo-num" style="top:163px">525</div>
  <svg class="trash" style="top:156px" viewBox="0 0 14 17" fill="none" stroke="#6688db" stroke-width="1.3"><path d="M1 3h12M5 3V1h4v2M2.5 3l1 13h7l1-13M5.5 6v8M8.5 6v8"/></svg>
  <div class="divider" style="top:204px"></div>
  <div class="wo-code" style="top:224px">TH1232-B</div><div class="wo-type" style="top:224px">SAR</div>
  <div class="wo-date" style="top:246px">2017-10-25</div><div class="wo-num" style="top:246px">112</div>
  <svg class="trash" style="top:237px" viewBox="0 0 14 17" fill="none" stroke="#6688db" stroke-width="1.3"><path d="M1 3h12M5 3V1h4v2M2.5 3l1 13h7l1-13M5.5 6v8M8.5 6v8"/></svg>
  <div class="divider" style="top:279px"></div>
</section>

<!-- Closed work orders -->
<section class="screen s-closed">
  <div class="scene head-pink" role="img" aria-label="Header illustration of a telecom tower and city skyline in pink tones"></div>
  <svg class="back" style="top:38px" viewBox="0 0 18 14" fill="none" stroke="#fff" stroke-width="1.6"><path d="M17 7H2M7 1L1 7l6 6"/></svg>
  <div class="brand" style="left:44px;top:33px">Veko</div>
  <div class="header-title" style="top:78px">Closed Work Orders</div>
  <div class="wo-code" style="top:148px">TH2236-A</div><div class="wo-type" style="top:148px">SAR</div>
  <div class="wo-date" style="top:170px">2017-10-25</div><div class="wo-num" style="top:170px">121</div>
  <svg class="trash" style="top:156px" viewBox="0 0 14 17" fill="none" stroke="#6688db" stroke-width="1.3"><path d="M1 3h12M5 3V1h4v2M2.5 3l1 13h7l1-13M5.5 6v8M8.5 6v8"/></svg>
  <div class="divider" style="top:204px"></div>
  <div class="wo-code" style="top:224px">TH1538-C</div><div class="wo-type" style="top:224px">SAR</div>
  <div class="wo-date" style="top:246px">2017-9-18</div><div class="wo-num" style="top:246px">224</div>
  <svg class="trash" style="top:233px" viewBox="0 0 14 17" fill="none" stroke="#6688db" stroke-width="1.3"><path d="M1 3h12M5 3V1h4v2M2.5 3l1 13h7l1-13M5.5 6v8M8.5 6v8"/></svg>
  <div class="divider" style="top:279px"></div>
</section>

<!-- Inspection form -->
<section class="screen s-form">
  <div class="scene head-form" role="img" aria-label="Header illustration of a telecom tower with clouds"></div>
  <svg class="back" style="top:38px" viewBox="0 0 18 14" fill="none" stroke="#fff" stroke-width="1.6"><path d="M17 7H2M7 1L1 7l6 6"/></svg>
  <div class="brand" style="left:44px;top:33px">Veko</div>
  <div class="q-title" style="top:85px"><span>001-</span> TSSR&nbsp; Approved ?</div>
  <div class="tools" style="top:121px">
    <svg viewBox="0 0 16 16"><rect x="1" y="4" width="14" height="10" rx="1.5" fill="#6688db"/><rect x="5" y="2" width="6" height="3" fill="#6688db"/><circle cx="8" cy="9" r="3" fill="#fff"/><circle cx="8" cy="9" r="1.6" fill="#6688db"/></svg>
    <svg viewBox="0 0 16 16"><path d="M8 15s-5-5.5-5-9a5 5 0 0 1 10 0c0 3.5-5 9-5 9z" fill="#6688db"/><circle cx="8" cy="6" r="1.8" fill="#fff"/></svg>
    <svg viewBox="0 0 16 16" fill="none" stroke="#6688db" stroke-width="1.3"><path d="M1 14h14M1 14L12 4M7 14a5 5 0 0 0-2-3"/></svg>
    <svg viewBox="0 0 16 16"><path d="M3 3h8l2 4v7H6L3 10z" fill="#6688db"/></svg>
    <svg viewBox="0 0 16 16" fill="#6688db"><rect x="1" y="3" width="2" height="2"/><rect x="5" y="3" width="10" height="2"/><rect x="1" y="7" width="2" height="2"/><rect x="5" y="7" width="10" height="2"/><rect x="1" y="11" width="2" height="2"/><rect x="5" y="11" width="10" height="2"/></svg>
  </div>
  <div class="comment" style="top:155px">Comment</div>
  <div class="divider" style="top:206px"></div>
  <div class="q-title" style="top:225px"><span>002-</span> Site Coordinate</div>
  <div class="tools" style="top:261px">
    <svg viewBox="0 0 16 16"><rect x="1" y="4" width="14" height="10" rx="1.5" fill="#6688db"/><rect x="5" y="2" width="6" height="3" fill="#6688db"/><circle cx="8" cy="9" r="3" fill="#fff"/><circle cx="8" cy="9" r="1.6" fill="#6688db"/></svg>
    <svg viewBox="0 0 16 16"><path d="M8 15s-5-5.5-5-9a5 5 0 0 1 10 0c0 3.5-5 9-5 9z" fill="#6688db"/><circle cx="8" cy="6" r="1.8" fill="#fff"/></svg>
    <svg viewBox="0 0 16 16" fill="none" stroke="#6688db" stroke-width="1.3"><path d="M1 14h14M1 14L12 4M7 14a5 5 0 0 0-2-3"/></svg>
    <svg viewBox="0 0 16 16"><path d="M3 3h8l2 4v7H6L3 10z" fill="#6688db"/></svg>
    <svg viewBox="0 0 16 16" fill="#6688db"><rect x="1" y="3" width="2" height="2"/><rect x="5" y="3" width="10" height="2"/><rect x="1" y="7" width="2" height="2"/><rect x="5" y="7" width="10" height="2"/><rect x="1" y="11" width="2" height="2"/><rect x="5" y="11" width="10" height="2"/></svg>
  </div>
  <div class="comment" style="top:295px">Comment</div>
  <div class="divider" style="top:345px"></div>
  <div class="btn btn-save">Save</div>
  <div class="btn btn-close">Save and Close</div>
</section>

<!-- Saving state -->
<section class="screen s-saving">
  <div class="scene head-form" role="img" aria-label="Header illustration of a telecom tower with clouds"></div>
  <svg class="back" style="top:38px" viewBox="0 0 18 14" fill="none" stroke="#fff" stroke-width="1.6"><path d="M17 7H2M7 1L1 7l6 6"/></svg>
  <div class="brand" style="left:44px;top:33px">Veko</div>
  <div class="q-title" style="top:85px"><span>001-</span> TSSR&nbsp; Approved ?</div>
  <div class="comment" style="top:155px">Comment</div>
  <div class="divider" style="top:206px"></div>
  <div class="q-title" style="top:225px"><span>002-</span> Site Coordinate</div>
  <div class="comment" style="top:295px">Comment</div>
  <div class="divider" style="top:345px"></div>
  <div class="btn btn-save">Save</div>
  <div class="btn btn-close">Save and Close</div>
  <div class="overlay"></div>
  <div class="dialog">
    <svg viewBox="0 0 54 54" stroke-width="4" stroke-linecap="butt">
      <g stroke="#6688db"><path d="M27 3v14"/><path d="M9 10l10 10"/><path d="M3 27h14"/></g>
      <g stroke="#a9c4f5"><path d="M45 10L35 20"/><path d="M51 27H37"/><path d="M45 44L35 34"/><path d="M27 51V37"/><path d="M9 44l10-10"/></g>
    </svg>
    <div>Saving your WO</div>
  </div>
</section>

</body>
</html>
```